KDR Business Card

Keystone Draper Resources is a successful and reputable financial services company.Our main services are home loans, commercial loans, vehicle finance and equipment finance. We also do development finance for property developers. Our company is always evolving to always be an industry leader in best financial service practices with access to the largest range of lenders in the country.

We want the business card to reflect our national finance company. Modern, professional corporate image. At the same time the concept of Keystone Draper Resources is that we help build wealth for you but the process for the client is an enjoyable peaceful experience. Not stressful at all .....

Colors to be same as the logo .... gold silver black white as the options

On the reverse side of the card I wanted either just the logo symbol or the logo symbol and text of the logo ....

It could be on a black background ..... or silver or gold .... want it to be quite striking to look at when you first see the card.

On the other side of the card I wanted the following details:

Martin Haldane
Director

0438 927 604

martin@kdrgrp.com.au

Po Box 718
Ferndale ACT 2614

www.kdrgrp.com.au

ACN 618 204 957 (This can be in very small print and can be in the bottom corner of the card or somewhere not very prominent)

As requested Ive uploaded the logo file in both .ai and .pdf formats. Please let me know if you need anything else. Thanks

Reason: Still deciding on which design I like best. I will provide individual feedback as well.

```html
<!DOCTYPE html>
<html lang="en">
<head>
<meta charset="utf-8">
<title>KDR Business Card</title>
<link href="https://fonts.googleapis.com/css2?family=Carlito:wght@400;700&display=swap" rel="stylesheet">
<style>
  :root {
    --page-bg: #0a0b0d;
    --card-bg: #030303;
    --gold: #d9b53a;
    --gold-light: #f1dd5c;
    --gold-deep: #c99a1d;
    --silver: #8d8d8d;
    --silver-light: #e4e4e2;
    --ink: #0a0a0a;
    --mark: #dedede;
  }
  * { margin: 0; padding: 0; box-sizing: border-box; }
  html, body {
    width: 763px; height: 1200px; overflow: hidden;
    background: var(--page-bg);
    font-family: "Carlito", "Calibri", Arial, sans-serif;
  }
  .canvas { position: relative; width: 763px; height: 1200px; }
  .card {
    position: absolute; left: 22px; width: 718px; height: 537px;
    background: var(--card-bg);
    border: 1px solid var(--gold-deep);
    border-radius: 22px;
    overflow: hidden;
  }
  .card--front { top: 22px; }
  .card--back { top: 640px; }
  .wave { position: absolute; inset: 0; width: 100%; height: 100%; }
  .brand { position: absolute; text-align: center; }
  .brand__mark {
    display: block; margin: 0 auto;
    width: 112px; height: 112px; border-radius: 50%;
    background: var(--mark);
    border: 5px solid var(--silver);
  }
  .brand__name {
    display: block; margin-top: 30px;
    color: var(--gold);
    font-size: 28px; font-weight: 400; letter-spacing: 1px;
    white-space: nowrap;
  }
  .card--front .brand { left: 0; width: 408px; top: 82px; }
  .card--back .brand { left: 0; width: 100%; top: 166px; }
  .contact {
    position: absolute; right: 46px; top: 286px;
    text-align: right; color: var(--ink);
    font-size: 18px; line-height: 21px;
  }
  .contact__name { font-size: 30px; font-weight: 700; line-height: 32px; }
  .contact__role { font-size: 21px; line-height: 24px; margin-bottom: 17px; }
  .contact__group { margin-bottom: 10px; }
  .back-web {
    position: absolute; left: 0; width: 100%; top: 443px;
    text-align: center; color: var(--gold);
    font-size: 15px; letter-spacing: 0.5px;
  }
</style>
</head>
<body>
<main class="canvas">
  <section class="card card--front">
    <svg class="wave" viewBox="0 0 800 598" preserveAspectRatio="none" aria-hidden="true">
      <defs>
        <linearGradient id="goldBand" x1="0" y1="1" x2="1" y2="0">
          <stop offset="0" stop-color="#c99a1d"/>
          <stop offset="0.6" stop-color="#f1dd5c"/>
          <stop offset="1" stop-color="#e7c536"/>
        </linearGradient>
        <linearGradient id="silverBand" x1="0" y1="0" x2="1" y2="0">
          <stop offset="0" stop-color="#7d7d7d"/>
          <stop offset="1" stop-color="#9a9a9a"/>
        </linearGradient>
      </defs>
      <path d="M0,530 C250,522 350,430 480,282 C560,192 650,132 800,118 L800,598 L0,598Z" fill="url(#silverBand)"/>
      <path d="M0,565 C262,556 372,462 500,306 C580,214 672,170 800,158 L800,598 L0,598Z" fill="#e4e4e2"/>
      <path d="M0,595 C282,588 392,492 520,336 C600,244 692,206 800,190 L800,598 L0,598Z" fill="url(#goldBand)"/>
    </svg>
    <div class="brand">
      <span class="brand__mark"></span>
      <span class="brand__name">Keystone Draper Resources</span>
    </div>
    <div class="contact">
      <p class="contact__name">Martin Haldane</p>
      <p class="contact__role">Director</p>
      <div class="contact__group">
        <p>Po Box 718</p>
        <p>Ferndale ACT 2614</p>
      </div>
      <p class="contact__group">0438 927 604</p>
      <div>
        <p>martin@kdrgrp.com.au</p>
        <p>www.kdrgrp.com.au</p>
      </div>
    </div>
  </section>

  <section class="card card--back">
    <div class="brand">
      <span class="brand__mark"></span>
      <span class="brand__name">Keystone Draper Resources</span>
    </div>
    <p class="back-web">www.kdrgrp.com.au</p>
  </section>
</main>
</body>
</html>
```